Business Card Design Project

I want my business cards to stand and feel timeless! I also want people to get their hands on them and freak out over how cool these are, I already have a logo i just want a very cool card design! this is for a makeup artist and maybe one day a line of cosmetics.

Target Market(s)

I want this to target women from 18 to 45

Industry/Entity Type

Business

Font styles to use
Decorative
Script

Colors

Designer to choose colors to be used in the design.

Requirements
Must have
• it must be elegante

```html
<!DOCTYPE html>
<html lang="en">
<head>
<meta charset="utf-8">
<title>Mara Quinn – Business Cards</title>
<link rel="stylesheet" href="https://fonts.googleapis.com/css2?family=Lato:wght@300;400;700&display=swap">
<style>
  :root {
    --page: #ecebe8;
    --card-white: #ffffff;
    --card-blue: #0d4b82;
    --logo-on-blue: #0a3a66;
    --ink: #222222;
    --ink-soft: #444444;
    --logo-ink: #555555;
    --band-navy: #1d5a94;
    --band-sky: #1a9ad0;
    --band-red: #d9233f;
    --band-grey: #8a9aa6;
    --band-white: #ffffff;
    --icon-purple: #b66fc2;
    --icon-pink: #e04a8a;
    --icon-orange: #f08a3c;
  }
  * { box-sizing: border-box; margin: 0; padding: 0; }
  html, body { width: 1200px; height: 1023px; overflow: hidden; }
  body {
    background: var(--page);
    font-family: "Lato", Arial, sans-serif;
    color: var(--ink);
    position: relative;
  }
  .card {
    position: absolute;
    left: 250px;
    width: 700px;
    height: 400px;
    border-radius: 22px;
    overflow: hidden;
    box-shadow: 0 6px 20px rgba(0,0,0,0.15);
  }
  .card--front { top: 60px; background: var(--card-white); }
  .card--back { top: 563px; background: var(--card-blue); }

  .band {
    position: absolute;
    left: 0; right: 0;
    height: 16px;
    display: flex;
  }
  .card--front .band { bottom: 0; }
  .card--back .band { top: 0; }
  .band span { display: block; height: 100%; }
  .band .navy { background: var(--band-navy); }
  .band .sky { background: var(--band-sky); }
  .band .red { background: var(--band-red); }
  .band .grey { background: var(--band-grey); }
  .band .white { background: var(--band-white); }

  .wordmark {
    position: absolute;
    font-weight: 300;
    text-transform: uppercase;
    letter-spacing: 6px;
    white-space: nowrap;
  }
  .card--front .wordmark {
    top: 70px; left: 270px;
    font-size: 46px;
    color: var(--logo-ink);
  }
  .card--back .wordmark {
    top: 168px; left: 0; right: 0;
    text-align: center;
    font-size: 52px;
    color: var(--logo-on-blue);
  }

  .holder {
    position: absolute;
    left: 40px; top: 220px;
  }
  .holder-name { font-size: 22px; font-weight: 700; color: var(--ink-soft); }
  .holder-title { font-size: 17px; font-weight: 700; color: var(--ink-soft); }

  .contacts {
    position: absolute;
    left: 270px; top: 268px;
    list-style: none;
  }
  .contacts li {
    display: flex;
    align-items: center;
    gap: 6px;
    font-size: 19px;
    line-height: 26px;
    color: var(--ink);
  }
  .contact-icon {
    width: 22px; height: 22px;
    display: flex; align-items: center; justify-content: center;
    border-radius: 3px;
  }
  .contact-icon--phone { background: var(--icon-purple); }
  .contact-icon--mobile { background: var(--icon-pink); }
  .contact-icon--mail { background: var(--icon-orange); }

  .address {
    position: absolute;
    right: 30px; top: 290px;
    text-align: left;
    font-size: 17px;
    font-weight: 700;
    line-height: 24px;
    color: var(--ink);
  }
</style>
</head>
<body>

  <section class="card card--front" aria-label="Business card front">
    <div class="wordmark">Mara Quinn</div>

    <div class="holder">
      <p class="holder-name">Mara Quinn</p>
      <p class="holder-title">Mackapiest</p>
    </div>

    <ul class="contacts">
      <li>
        <span class="contact-icon contact-icon--phone">
          <svg width="14" height="14" viewBox="0 0 14 14" aria-hidden="true"><path d="M3 1.5 L5 1.5 L6 4.2 L4.6 5.2 Q5.6 7.6 8.8 9.4 L9.8 8 L12.5 9 L12.5 11 Q12.5 12.5 11 12.5 Q2 12 1.5 3 Q1.5 1.5 3 1.5Z" fill="#fff"/></svg>
        </span>1-555-014-3870
      </li>
      <li>
        <span class="contact-icon contact-icon--mobile">
          <svg width="14" height="14" viewBox="0 0 14 14" aria-hidden="true"><rect x="3.5" y="1" width="7" height="12" rx="1.2" fill="none" stroke="#fff" stroke-width="1.4"/><circle cx="7" cy="11" r="0.8" fill="#fff"/></svg>
        </span>1-555-019-2264
      </li>
      <li>
        <span class="contact-icon contact-icon--mail">
          <svg width="14" height="14" viewBox="0 0 14 14" aria-hidden="true"><rect x="1.5" y="3" width="11" height="8" fill="none" stroke="#fff" stroke-width="1.3"/><path d="M1.5 3 L7 7.5 L12.5 3" fill="none" stroke="#fff" stroke-width="1.3"/></svg>
        </span>hello@maraquinn.com
      </li>
    </ul>

    <p class="address">000 Linden Row,<br>Fairhaven, NJ 07000</p>

    <div class="band">
      <span class="navy" style="width:40%"></span>
      <span class="sky" style="width:22%"></span>
      <span class="red" style="width:24%"></span>
      <span class="grey" style="width:14%"></span>
    </div>
  </section>

  <section class="card card--back" aria-label="Business card back">
    <div class="band">
      <span class="white" style="width:12%"></span>
      <span class="sky" style="width:30%"></span>
      <span class="red" style="width:26%"></span>
      <span class="grey" style="width:32%"></span>
    </div>
    <div class="wordmark">Mara Quinn</div>
  </section>

</body>
</html>
```